2024 Ridgeway Financial Team Deck

I have created a power point slide deck and I need the slide deck recreated. Organized, with better color, background pictures, etc. I am thinking the colors for the presentation can be navy blue, and white, and gold, with hints of silver and black. We are financial planning firm that specializes in working with tech companies in silicon valley.

```html
<!DOCTYPE html>
<html lang="en">
<head>
<meta charset="utf-8">
<title>Ridgeway Financial 2024 – Team Deck</title>
<link href="https://fonts.googleapis.com/css2?family=Poppins:wght@400;500;600&display=swap" rel="stylesheet">
<style>
:root{
  --navy:#1c2a55;
  --blue:#0b6cc6;
  --frame:#1b3ca6;
  --ink:#222a3a;
  --muted:#3c4456;
  --bullet:#6a78a6;
  --green:#9ccc2e;
  --pink:#e8197f;
  --grid:#e3e6ec;
  --teal:#1cb59a;
}
*{margin:0;padding:0;box-sizing:border-box}
html,body{width:1200px;height:1101px;overflow:hidden;background:#fff}
body{font-family:"Poppins",sans-serif;color:var(--ink);position:relative}
.slide{position:absolute;width:513px;height:288px;background:#fff;overflow:hidden;box-shadow:0 6px 22px rgba(20,30,60,.13)}
.col-left{left:71px}.col-right{left:623px}
.row-1{top:64px}.row-2{top:397px}.row-3{top:733px}
.slide-title{position:absolute;top:7px;left:0;width:100%;text-align:center;font-size:17px;font-weight:500;letter-spacing:-.1px}
.footer{position:absolute;left:0;bottom:0;width:100%;height:20px;display:flex}
.footer-url{width:189px;background:var(--navy);color:#fff;font-size:6.4px;padding-left:18px;display:flex;align-items:center}
.footer-title{width:137px;text-align:center;font-size:9.6px;font-weight:500;white-space:nowrap;display:flex;align-items:center;justify-content:center}
.footer-page{flex:1;background:var(--navy);color:#fff;font-size:6.2px;font-weight:500;padding-left:28px;display:flex;align-items:center}
.bullets{list-style:none}
.bullets li{position:relative;padding-left:11px}
.bullets li::before{content:"";position:absolute;left:0;top:3px;width:4px;height:4px;border:1px solid var(--bullet);border-radius:50%}
.photo{position:absolute}
.photo-frame{position:absolute;border:2px solid var(--frame)}
.accent-tick{position:absolute;right:0;top:0;width:1px;height:22px;background:var(--teal)}

/* cover */
.cover-bg{position:absolute;inset:0;background:linear-gradient(135deg,#eef2f7 0%,#f7f8fb 45%,#eef1f6 100%);opacity:.9}
.cover-title{position:absolute;top:79px;width:100%;text-align:center;font-size:25px;font-weight:500;color:#1b1f2b}
.pill{position:absolute;left:185px;width:143px;height:27px;background:var(--blue);color:#fff;font-size:9px;font-weight:500;display:flex;align-items:center;justify-content:center;gap:6px;white-space:nowrap}
.pill-url{top:127px;border-radius:14px}
.pill-phone{top:261px;border-radius:14px 14px 0 0}
.cover-sub{position:absolute;top:174px;width:100%;text-align:center;font-size:13px;font-weight:500}
.cover-small{position:absolute;top:194px;width:100%;text-align:center;font-size:8.4px}

/* mission */
.mission-line{position:absolute;top:35px;width:100%;text-align:center;font-size:8.4px;font-weight:500}
.mission-body{position:absolute;left:262px;top:54px;width:200px;font-size:6.6px;line-height:10.2px;color:var(--muted)}
.mission-body p{margin-bottom:10px}
.mission-body li{margin-bottom:8.5px}

/* vision */
.vision-sub{position:absolute;top:31px;width:100%;text-align:center;font-size:8.6px}
.vision-col{position:absolute;top:52px;font-size:6.6px;line-height:10.1px;color:var(--muted)}
.vision-col li{margin-bottom:9px}
.vision-left{left:11px;width:248px}
.vision-right{left:267px;width:240px}

/* chart */
.chart{position:absolute;left:0;top:0}

/* functions */
.intro{position:absolute;top:39px;left:10px;width:493px;text-align:center;font-size:8.2px;line-height:14.4px;font-weight:500;letter-spacing:-.1px}
.person{position:absolute}
.person h3{font-size:11px;font-weight:500;margin-bottom:2px}
.person li{font-size:6.8px;line-height:12.6px;color:var(--muted);white-space:nowrap}
.person li::before{top:4px}
.person-compact li{font-size:6.3px}
</style>
</head>
<body>

<!-- Cover -->
<section class="slide col-left row-1">
  <div class="cover-bg" role="img" aria-label="Faint overhead photo of a team around a desk with charts, papers and a calculator"></div>
  <h1 class="cover-title">Ridgeway Financial 2024</h1>
  <div class="pill pill-url">www.ridgewayfinancial.com</div>
  <p class="cover-sub">Perspiciatis unde omnis isteatu</p>
  <p class="cover-small">Kaseinpiciatis unde omnis isteatu</p>
  <div class="pill pill-phone">
    <svg width="7" height="7" viewBox="0 0 24 24" aria-hidden="true"><path fill="#fff" d="M6.6 10.8a15.1 15.1 0 0 0 6.6 6.6l2.2-2.2a1 1 0 0 1 1-.25 11.4 11.4 0 0 0 3.6.57 1 1 0 0 1 1 1V20a1 1 0 0 1-1 1A17 17 0 0 1 3 4a1 1 0 0 1 1-1h3.5a1 1 0 0 1 1 1c0 1.25.2 2.45.57 3.57a1 1 0 0 1-.25 1z"/></svg>
    <span>+1 555 010 2024</span>
  </div>
</section>

<!-- Mission -->
<section class="slide col-right row-1">
  <h2 class="slide-title">Mission Statement</h2>
  <p class="mission-line">To provide our client with the systems and processes needed to Guide their Hero’s journey and leave an Impact</p>
  <div class="photo" style="left:37px;top:66px;width:201px;height:182px;background:linear-gradient(135deg,#2b3a55,#8a98ad 55%,#d9dee6)" role="img" aria-label="Photo of advisors reviewing charts on a tablet and paper reports"></div>
  <div class="photo-frame" style="left:26px;top:59px;width:200px;height:181px"></div>
  <div class="mission-body">
    <p>The Hero’s Journey: We believe everyone has a purpose, God’s purpose in their life, and it is our mission to help our clients relentlessly pursue their purpose. A life with purpose is a life living out your Hero’s Journey!</p>
    <ul class="bullets">
      <li>Our financial planning &amp; wealth management services give our clients</li>
      <li>More Time &amp; Clarity on their plan and what is needed to accomplish the objective</li>
      <li>We help our clients think bigger and professionally hold them accountable to their goals</li>
      <li>We help reduce taxes drag , increase diversification, reduce investment risk, &amp; maximize investment returns so that our clients have the financial resources to maximize their potential and ultimately leave a larger Impact on the world.</li>
    </ul>
  </div>
  <div class="footer"><div class="footer-url">www.ridgewayfinancial.com</div><div class="footer-title">Ridgeway Financial 2024</div><div class="footer-page">Page 02</div></div>
</section>

<!-- Firm Vision -->
<section class="slide col-left row-2">
  <h2 class="slide-title">Firm Vision</h2>
  <p class="vision-sub">(December 2026)</p>
  <ul class="bullets vision-col vision-left">
    <li>We are an elite wealth management firm at Harborline Mutual, that is impact driven and focused on the clients’ goals, needs, and objectives above all else. We specialize in serving Executives, Directors, &amp; Vice Presidents at Orchard, Searchly, Nexa, &amp; other tech companies where a heavy part of compensation is coming in the form of stock (RSU/ESPP).</li>
    <li>Over the last 3 years we have grown the firm organically, through introductions, and seminars/speaking events.</li>
    <li>We are the primary advisory firm &amp; financial planning relationship for 300 households in this space. We manage over $150m in assets and our minimize account size has grown to $500k. We are consistently qualifying for forum and this year (awards year 2026) we will have $1M premium and $1M GDC in just 8 years at Harborline Mutual.</li>
    <li>Our team has 3 lead advisors that are each fully responsible for servicing a sleeve of 80 – 125 clients on an annual basis. Each advisor is also responsible for bringing on an additional $6M of AUM annually, 10 new clients, and writing $150k of premium.</li>
  </ul>
  <ul class="bullets vision-col vision-right">
    <li>Our team has a mandatory team trip every year, we don’t work weekends, we rarely work past 5pm, and we have frogman Fridays. Every Friday the team is off by 1pm at the latest, we get in, get shit done, and get out.</li>
    <li style="margin-bottom:13px">Richard is only taking client meetings 4 days/week and takes no more then 16 on any given week. He has a 2nd chair in every meeting that is taking notes and will be responsible for the follow up. The calendar is filled by the lead advisors who are working on a path to partnership at the firm. Everyone is financially tied to bottom line revenue. We have a team of winners!</li>
    <li style="margin-bottom:10px">We are healthy, fit, &amp; happy. We have the opportunity to help who we want when we want. We have control over our lives and work schedule. We dictate the pace and cadence that we want to move at based on our goals any given year. Every member of the team loves the team, supports the mission, and wants to leave an impact.</li>
    <li>We are well on our way to managing $1B by December 2033</li>
  </ul>
  <div class="footer"><div class="footer-url">www.ridgewayfinancial.com</div><div class="footer-title">Ridgeway Financial 2024</div><div class="footer-page">Page 03</div></div>
</section>

<!-- Org Chart -->
<section class="slide col-right row-2">
  <div class="accent-tick"></div>
  <h2 class="slide-title">Current Org Chart</h2>
  <svg class="chart" width="513" height="288" viewBox="0 0 856 481" aria-label="Line chart of two series across twelve months">
    <g stroke="var(--grid)" stroke-width="1">
      <line x1="89" y1="112" x2="781" y2="112"/><line x1="89" y1="135.6" x2="781" y2="135.6"/><line x1="89" y1="159.2" x2="781" y2="159.2"/><line x1="89" y1="182.8" x2="781" y2="182.8"/><line x1="89" y1="206.4" x2="781" y2="206.4"/><line x1="89" y1="230" x2="781" y2="230"/><line x1="89" y1="253.6" x2="781" y2="253.6"/><line x1="89" y1="277.2" x2="781" y2="277.2"/><line x1="89" y1="300.8" x2="781" y2="300.8"/><line x1="89" y1="324.4" x2="781" y2="324.4"/><line x1="89" y1="348" x2="781" y2="348"/>
      <line x1="89" y1="112" x2="89" y2="348"/><line x1="146.7" y1="112" x2="146.7" y2="348"/><line x1="204.3" y1="112" x2="204.3" y2="348"/><line x1="262" y1="112" x2="262" y2="348"/><line x1="319.7" y1="112" x2="319.7" y2="348"/><line x1="377.3" y1="112" x2="377.3" y2="348"/><line x1="435" y1="112" x2="435" y2="348"/><line x1="492.7" y1="112" x2="492.7" y2="348"/><line x1="550.3" y1="112" x2="550.3" y2="348"/><line x1="608" y1="112" x2="608" y2="348"/><line x1="665.7" y1="112" x2="665.7" y2="348"/><line x1="723.3" y1="112" x2="723.3" y2="348"/><line x1="781" y1="112" x2="781" y2="348"/>
    </g>
    <g font-family="Poppins, sans-serif" font-size="7" fill="#444" text-anchor="end">
      <text x="80" y="114">100</text><text x="80" y="138">90</text><text x="80" y="161">80</text><text x="80" y="185">70</text><text x="80" y="208">60</text><text x="80" y="232">50</text><text x="80" y="256">40</text><text x="80" y="279">30</text><text x="80" y="303">20</text><text x="80" y="326">10</text><text x="80" y="350">0</text>
    </g>
    <g font-family="Poppins, sans-serif" font-size="7" fill="#444" text-anchor="middle">
      <text x="117" y="364">JAN</text><text x="175" y="364">FEB</text><text x="232" y="364">MAR</text><text x="290" y="364">APR</text><text x="348" y="364">MAY</text><text x="406" y="364">JUN</text><text x="463" y="364">JUL</text><text x="521" y="364">AUG</text><text x="579" y="364">SEP</text><text x="636" y="364">OCT</text><text x="694" y="364">NOV</text><text x="752" y="364">DEC</text>
    </g>
    <polyline fill="none" stroke="var(--green)" stroke-width="1.6" points="89,253.6 146.7,230 204.3,253.6 262,182.8 319.7,182.8 377.3,206.4 435,182.8 492.7,182.8 550.3,145 608,135.6 665.7,135.6 723.3,145 781,135.6"/>
    <g fill="var(--green)"><circle cx="89" cy="253.6" r="3"/><circle cx="146.7" cy="230" r="3"/><circle cx="204.3" cy="253.6" r="3"/><circle cx="262" cy="182.8" r="3"/><circle cx="319.7" cy="182.8" r="3"/><circle cx="377.3" cy="206.4" r="3"/><circle cx="435" cy="182.8" r="3"/><circle cx="492.7" cy="182.8" r="3"/><circle cx="550.3" cy="145" r="3"/><circle cx="608" cy="135.6" r="3"/><circle cx="665.7" cy="135.6" r="3"/><circle cx="723.3" cy="145" r="3"/><circle cx="781" cy="135.6" r="3"/></g>
    <polyline fill="none" stroke="var(--pink)" stroke-width="1.6" points="89,324.4 146.7,277.2 204.3,300.8 262,230 319.7,206.4 377.3,253.6 435,230 492.7,253.6 608,159.2 723.3,206.4 781,159.2"/>
    <g fill="var(--pink)"><circle cx="89" cy="324.4" r="3"/><circle cx="146.7" cy="277.2" r="3"/><circle cx="204.3" cy="300.8" r="3"/><circle cx="262" cy="230" r="3"/><circle cx="319.7" cy="206.4" r="3"/><circle cx="377.3" cy="253.6" r="3"/><circle cx="435" cy="230" r="3"/><circle cx="492.7" cy="253.6" r="3"/><circle cx="608" cy="159.2" r="3"/><circle cx="723.3" cy="206.4" r="3"/><circle cx="781" cy="159.2" r="3"/></g>
  </svg>
  <div class="footer"><div class="footer-url">www.ridgewayfinancial.com</div><div class="footer-title">Ridgeway Financial 2024</div><div class="footer-page">Page 04</div></div>
</section>

<!-- Vital Functions -->
<section class="slide col-left row-3">
  <h2 class="slide-title">Vital Functions</h2>
  <p class="intro">These are 3 vital functions on the leverage curve that you need to drive massive results and make it rain. Like Dale Hartman say’s if we can focus on these 3 things and eliminate all other distractions we can accomplish anything!</p>
  <div class="person" style="left:139px;top:92px"><h3>Richard</h3><ul class="bullets"><li>Client Meeting</li><li>Dial</li><li>Business Development</li></ul></div>
  <div class="person" style="left:309px;top:92px"><h3>Moreno</h3><ul class="bullets"><li>Investment Processing</li><li>Final Case Prep/Executive Summary</li><li>Service Existing Book</li></ul></div>
  <div class="person" style="left:139px;top:169px"><h3>Stella</h3><ul class="bullets"><li>Insurance Processing</li><li>Calendar Management for Richard</li><li>OCI Manager for Richard</li></ul></div>
  <div class="person" style="left:310px;top:169px"><h3>Jonah</h3><ul class="bullets"><li>Activity Numbers &amp; reporting</li><li>Financials / Bookkeeping</li><li>Team Project Manger</li></ul></div>
  <div class="footer"><div class="footer-url">www.ridgewayfinancial.com</div><div class="footer-title">Ridgeway Financial 2024</div><div class="footer-page">Page 05</div></div>
</section>

<!-- Leadership -->
<section class="slide col-right row-3">
  <div class="accent-tick"></div>
  <h2 class="slide-title">Leadership Responsibilities</h2>
  <div class="photo" style="left:15px;top:52px;width:214px;height:191px;background:linear-gradient(135deg,#c9d3e6,#eef1f7 45%,#a9b6cf)" role="img" aria-label="Photo of a hand with a pen working a calculator over financial charts"></div>
  <div class="photo-frame" style="left:8px;top:45px;width:213px;height:190px"></div>
  <div class="person person-compact" style="left:245px;top:78px"><h3>Richard</h3><ul class="bullets"><li>Serving A+ A Clients</li></ul></div>
  <div class="person person-compact" style="left:386px;top:78px"><h3>Moreno</h3><ul class="bullets"><li>Richard's Calendar Management</li><li>Insurance Operations</li><li>Annual Reviews</li></ul></div>
  <div class="person person-compact" style="left:245px;top:155px"><h3>Moreno</h3><ul class="bullets"><li>Servicing B &amp; C Clients</li><li>New Investments account onboarding</li><li>Case Prep</li></ul></div>
  <div class="person person-compact" style="left:387px;top:155px"><h3>Jonah</h3><ul class="bullets"><li>Posting and Planning</li><li>Goal Tracking</li></ul></div>
  <div class="footer"><div class="footer-url">www.ridgewayfinancial.com</div><div class="footer-title">Ridgeway Financial 2024</div><div class="footer-page">Page 06</div></div>
</section>

</body>
</html>
```